Flyer-Design für Baumfällungen und -pflege
Zielgruppe
Wir bieten Baumpflege und Baumfällungen an. Das Design sollte hochwertig, schlicht und sympathisch sein. Zielgruppe sind Eigentümer von Bäumen jeglichen Alters.
Aufgabenstellung
Homepage: www.astkrone-dienst.com
Logo bitte vorerst von der Homepage verwenden. Ich habe die Datei noch nicht, kann sie aber besorgen, Bilder kann ich auch noch liefern bei Bedarf. Text kann auch, am Besten in abgespeckter Form oder nur die Überschriften z.B. der Leistungen, von Homepage verwendet werden.
Flyer und Design sollen sein:
- sympathisch
- vertrauensvoll
- professionell
- übersichtlich
- handlich

```html
<!DOCTYPE html>
<html lang="de">
<head>
<meta charset="utf-8">
<title>Astkrone Flyer</title>
<link rel="stylesheet" href="https://fonts.googleapis.com/css2?family=Montserrat:wght@500;600;700&family=Open+Sans:wght@400;600&display=swap">
<style>
:root{
  --bg:#e9e9e7;
  --paper:#f2f1ee;
  --beige:#efe3d0;
  --brown:#5b524b;
  --orange:#e38a2a;
  --green:#55a443;
  --green-dark:#2f7d32;
  --text:#3c3835;
  --sky:#5b8fc9;
}
*{box-sizing:border-box;margin:0;padding:0}
html,body{width:1200px;height:857px;overflow:hidden;background:var(--bg)}
body{font-family:"Open Sans",sans-serif;color:var(--text);position:relative}
.sheet{position:absolute;top:225px;width:575px;height:407px;display:flex;box-shadow:0 4px 14px rgba(0,0,0,.12)}
.sheet-inside{left:17px;background:var(--beige)}
.sheet-outside{left:608px;background:var(--paper)}
.panel{flex:1;position:relative;overflow:hidden}
.panel+.panel{border-left:1px solid rgba(0,0,0,.06)}
.media{display:block}
h2{font-family:"Montserrat",sans-serif;font-weight:700;color:var(--orange);text-transform:uppercase;line-height:1.1}
p{font-size:5.6px;line-height:1.45}

/* inside: services */
.services-title{font-size:13px;padding:18px 0 0 12px}
.service-grid{display:grid;grid-template-columns:1fr 1fr;gap:10px 8px;padding:12px 10px}
.service .illustration{width:100%;height:52px;border-radius:6px;background:radial-gradient(circle,#8fbf6a 0 40%,#e8c79a 41% 60%,transparent 61%)}
.service h3{font-family:"Montserrat",sans-serif;font-size:6px;font-weight:600;color:var(--orange);margin:5px 0 3px}
.panel-services-2 .service-grid{padding-top:24px}
.service-wide{grid-column:1 / 3;width:60%;margin:0 auto}

.panel-story{display:flex}
.story-photos{width:42%;display:flex;flex-direction:column}
.story-photos .media{flex:1}
.story-text{width:58%;padding:44px 8px 0}
.story-text h3{font-family:"Montserrat",sans-serif;font-size:6px;font-weight:700;color:var(--orange);text-transform:uppercase;margin:8px 0 5px;line-height:1.3}
.leaf-sprig{position:absolute;top:6px;right:8px;width:66px;height:34px;border-radius:20px;background:linear-gradient(90deg,#8cc63f,#3f8f3a)}
.icon-dot{width:12px;height:12px;border-radius:50%;background:var(--orange)}

/* outside */
.panel-hello{display:flex}
.hello-photo{width:38%;height:100%;background:linear-gradient(180deg,#4f86c6,#7aa9d8 55%,#6a8a4c 85%,#4d6d35)}
.hello-text{width:62%;padding:18px 8px 0}
.hello-text h2{font-size:12px;margin-bottom:5px}
.hello-text h2.sub{font-size:10px;margin:9px 0 5px}
.grass{position:absolute;left:0;right:0;bottom:0;height:38px;background:linear-gradient(180deg,#7fc24a,#3e9136)}

.panel-contact{text-align:center}
.brand-block{background:var(--brown);height:130px;display:flex;align-items:center;justify-content:center;gap:6px}
.brand-mark{width:20px;height:20px;border:1.5px solid #fff}
.brand-name{font-family:"Montserrat",sans-serif;font-weight:600;font-size:15px;letter-spacing:1px;color:#fff}
.portrait{width:62px;height:62px;border-radius:50%;margin:-14px auto 12px;border:3px solid var(--orange);background:linear-gradient(180deg,#6ea0d6,#9bc06a);position:relative}
.contact-lines{font-family:"Montserrat",sans-serif;font-size:6px;letter-spacing:1.2px;text-transform:uppercase;line-height:1.7;color:var(--text)}
.contact-cta{font-family:"Montserrat",sans-serif;font-size:9px;font-weight:600;color:var(--orange);text-transform:uppercase;margin-top:12px;line-height:1.2}
.contact-phone{font-family:"Montserrat",sans-serif;font-size:15px;font-weight:600;color:var(--orange);margin-top:6px}
.contact-web{font-family:"Montserrat",sans-serif;font-size:6px;letter-spacing:1.6px;text-transform:uppercase;margin-top:6px}

.cover-brand{height:115px;display:flex;align-items:center;justify-content:center;gap:6px;position:relative}
.cover-brand .brand-mark{border-color:var(--orange);background:var(--orange)}
.cover-brand .brand-name{color:var(--brown)}
.cover-photo{height:182px;background:linear-gradient(180deg,#2f6fc0,#5c98d8 65%,#2f5d33)}
.cover-band{background:var(--brown);height:110px;padding:12px 14px;color:#fff}
.cover-band h1{font-family:"Montserrat",sans-serif;font-size:10px;font-weight:600;text-transform:uppercase;line-height:1.3;letter-spacing:.5px}
.cover-band .web{font-family:"Montserrat",sans-serif;font-size:5.5px;letter-spacing:1.4px;margin-top:6px;text-transform:uppercase}
</style>
</head>
<body>

<section class="sheet sheet-inside" aria-label="Innenseite">
  <div class="panel panel-services-1">
    <h2 class="services-title">Unsere Leistungen</h2>
    <div class="service-grid">
      <div class="service"><div class="illustration" role="img" aria-label="Illustration: Baumpfleger an einem großen Baum"></div><h3>Baumpflege nach ZTV</h3><p>Fachgerechter Schnitt für gesunde, sichere und langlebige Bäume.</p></div>
      <div class="service"><div class="illustration" role="img" aria-label="Illustration: Hochsitz am Baum"></div><h3>Seilklettertechnik</h3><p>Arbeiten in der Krone auch dort, wo keine Bühne hinkommt.</p></div>
      <div class="service"><div class="illustration" role="img" aria-label="Illustration: Kletterer in der Baumkrone"></div><h3>Kronenpflege und Auslichtung</h3><p>Mehr Licht und Stabilität durch gezielte Entnahme einzelner Äste.</p></div>
      <div class="service"><div class="illustration" role="img" aria-label="Illustration: Arbeiter mit Motorsäge"></div><h3>Totholzentfernung</h3><p>Abgestorbene Äste sicher entfernen und Gefahren vermeiden.</p></div>
    </div>
  </div>
  <div class="panel panel-services-2">
    <div class="service-grid">
      <div class="service"><div class="illustration" role="img" aria-label="Illustration: einzelner Laubbaum"></div><h3>Fällungen mit Seiltechnik</h3><p>Stückweise Abtragung auch auf engem Raum am Haus.</p></div>
      <div class="service"><div class="illustration" role="img" aria-label="Illustration: Motorsäge am Stamm"></div><h3>Sturmschäden und Notfälle</h3><p>Schnelle Hilfe nach Unwettern rund um die Uhr.</p></div>
      <div class="service"><div class="illustration" role="img" aria-label="Illustration: Kletterer am Stamm"></div><h3>Baumkontrolle</h3><p>Prüfung der Verkehrssicherheit mit klarem Bericht.</p></div>
      <div class="service"><div class="illustration" role="img" aria-label="Illustration: junge Obstbäume"></div><h3>Obstbaumschnitt</h3><p>Erziehungs- und Erhaltungsschnitt für reiche Ernte.</p></div>
      <div class="service service-wide"><div class="illustration" role="img" aria-label="Illustration: Häcksler mit Arbeiter"></div><h3>Häckseln und Abtransport</h3><p>Wir hinterlassen Ihren Garten sauber und aufgeräumt.</p></div>
    </div>
  </div>
  <div class="panel panel-story">
    <div class="story-photos">
      <div class="media" role="img" aria-label="Foto: Baumstammscheibe" style="background:linear-gradient(135deg,#b08660,#d9b48a)"></div>
      <div class="media" role="img" aria-label="Foto: Kletterer am hohen Stamm" style="background:linear-gradient(180deg,#5d93cf,#88aed8)"></div>
      <div class="media" role="img" aria-label="Foto: Fällung neben einem Haus" style="background:linear-gradient(180deg,#9aa4a8,#6c7a5a)"></div>
      <div class="media" role="img" aria-label="Foto: blauer Himmel mit Krone" style="background:linear-gradient(180deg,#3f7fcf,#6fa3dc)"></div>
    </div>
    <div class="story-text">
      <div class="icon-dot"></div>
      <h3>Zum Fällen bereit? Wir planen jeden Schritt mit Ihnen gemeinsam.</h3>
      <p>Jeder Baum ist anders. Deshalb schauen wir uns die Lage vor Ort genau an und besprechen mit Ihnen, welche Maßnahme sinnvoll ist. Ob Pflege oder Fällung – wir arbeiten sicher, sauber und mit Respekt vor Ihrem Grundstück und der Natur.</p>
    </div>
    <div class="leaf-sprig" role="img" aria-label="Illustration: grüner Blätterzweig"></div>
  </div>
</section>

<section class="sheet sheet-outside" aria-label="Außenseite">
  <div class="panel panel-hello">
    <div class="hello-photo" role="img" aria-label="Foto: Baumkletterer an einer hohen Fichte"></div>
    <div class="hello-text">
      <h2>Hallo</h2>
      <p>Ich bin Jonas Weidmann und kümmere mich mit meiner Firma Astkrone um Bäume jeden Alters. Sicherheit, Sorgfalt und Freude an der Arbeit stehen für mich an erster Stelle.</p>
      <h2 class="sub">Wie ich zur Baumpflege gekommen bin</h2>
      <p>Bäume begleiten mich schon seit meiner Kindheit. Nach meiner Ausbildung wollte ich draußen arbeiten und lernte das Klettern am Seil. Heute verbinde ich Technik und Erfahrung, um Ihre Bäume gesund zu erhalten oder sicher zu fällen. Jeder Einsatz ist für mich ein kleines Abenteuer in den Wipfeln unserer schönen Heimat.</p>
    </div>
    <div class="grass" role="img" aria-label="Illustration: grüne Grashalme"></div>
  </div>
  <div class="panel panel-contact">
    <div class="brand-block"><span class="brand-mark"></span><span class="brand-name">ASTKRONE</span></div>
    <div class="portrait" role="img" aria-label="Foto: Baumpfleger mit Helm"></div>
    <div class="contact-lines">Jonas Weidmann<br>Astkrone<br>79999 Tannweiler<br>jonas.weidmann@example.de</div>
    <div class="contact-cta">Ich freue mich<br>von Ihnen zu hören!</div>
    <div class="contact-phone">+49 151-00000000</div>
    <div class="contact-web">www.astkrone-dienst.com</div>
  </div>
  <div class="panel panel-cover">
    <div class="cover-brand">
      <span class="brand-mark"></span><span class="brand-name">ASTKRONE</span>
      <div class="leaf-sprig" role="img" aria-label="Illustration: grüner Blätterzweig"></div>
    </div>
    <div class="cover-photo" role="img" aria-label="Foto: Baumpfleger auf Hubarbeitsbühne vor blauem Himmel"></div>
    <div class="cover-band">
      <h1>Ihrem Profi für<br>Baumpflege im<br>Hochschwarzwald</h1>
      <div class="web">www.astkrone-dienst.com</div>
    </div>
  </div>
</section>

</body>
</html>
```